Pine Hill Drafting - Flyer Design

I'm looking for good designs of the 2 sided flyer size DL (210 x 95 mm)
Please make sure the design is in the same colours as my business card. Image attached.
Include Architectural plan at the background.
Please note that some words are in capital letters...
FRONT PAGE including :
Are you planning to RENOVATE, EXTEND the house, build new GRANNY FLAT?
Do you need assistance with DA , COMPLYING DEVELOPMENT?
Is your building budget tight and you DON'T WANT to spend it on the ARCHITECTURAL FEES?
For free obligation quote contact:
PINE HILL DRAFTING
pinehilldrafting@mailnest.net.au
Dorte - 0482 657 930
For more details check: www.pinehilldrafting.net.au
Follow us on chatterly: www.chatterly.net/pinehilldrafting
BACK PAGE including:
Services
- Building Design
- Architectural Drafting
- 3D Modelling
- Norvo Assessment
- Building Specifications
- Council Submission Services
- Coordination with Building Professionals
Contact Dorte on 0482 657 930 or pinehilldrafting@mailnest.net.au for obligation free quote

```html
<!DOCTYPE html>
<html lang="en">
<head>
<meta charset="utf-8">
<title>Pine Hill Drafting – DL Flyer</title>
<link href="https://fonts.googleapis.com/css2?family=Arimo:ital,wght@0,400;0,700;1,400;1,700&display=swap" rel="stylesheet">
<style>
:root{
  --sky:#17a6d7;
  --sky-text:#1b9fd4;
  --deep:#1b5870;
  --ink:#24475a;
  --paper:#ffffff;
  --page:#ffffff;
  --plan-light:#f3f6f8;
  --plan-mid:#d9e1e6;
}
*{margin:0;padding:0;box-sizing:border-box}
html,body{width:1200px;height:1101px;overflow:hidden;background:var(--page)}
body{position:relative;font-family:"Arimo",Arial,sans-serif;color:var(--ink)}
.flyer{position:absolute;left:65px;width:1053px;height:498px;background:var(--paper);box-shadow:0 2px 6px rgba(0,0,0,.35);overflow:hidden}
.flyer--front{top:22px}
.flyer--back{top:552px}
.masthead{position:absolute;left:0;top:0;width:100%;height:96px;background:var(--sky)}
.masthead__rule{position:absolute;left:0;top:96px;width:100%;height:12px;background:var(--deep)}
.brand{position:absolute;left:35px;top:26px;color:#fff;font-weight:700;font-size:50px;letter-spacing:.5px;line-height:1}
.plan-art{position:absolute;left:0;top:108px;width:280px;height:390px;background:linear-gradient(135deg,var(--plan-light),var(--plan-mid))}
.questions{position:absolute;left:300px;top:126px;width:465px;text-align:center;font-size:22.5px;line-height:29.5px;color:var(--ink)}
.questions p{margin-bottom:30px}
.hl{color:var(--sky-text);font-weight:700;font-style:italic}
.badge{position:absolute;left:808px;top:138px;width:204px;height:204px}
.badge__text{position:absolute;left:808px;top:180px;width:204px;text-align:center;color:#fff;font-weight:700;font-style:italic;font-size:19.5px;line-height:25.5px}
.contact{position:absolute;left:760px;top:348px;width:300px;text-align:center;font-size:16.5px;line-height:21px;color:var(--ink)}
.contact__name{font-weight:700;color:var(--deep)}
.footer-front{position:absolute;left:280px;top:454px;width:773px;height:44px;background:var(--sky);color:#fff;font-size:14.5px;line-height:19px;padding:3px 0 0 10px}
.house-art{position:absolute;left:55px;top:140px;width:440px;height:240px;background:linear-gradient(160deg,#f7f9fa,#e4e9ec)}
.services{position:absolute;left:540px;top:137px;font-size:21px;line-height:27.6px;color:var(--ink);list-style:none}
.services__title{font-style:italic;font-weight:700;font-size:27px;color:var(--deep);margin-bottom:0;line-height:32px}
.cta{position:absolute;left:0;top:386px;width:100%;text-align:center;color:var(--sky-text);font-weight:700;font-style:italic;font-size:21.5px;line-height:28px}
.footer-back{position:absolute;left:0;top:454px;width:100%;height:44px;background:var(--sky);color:#fff;font-size:15.5px;text-align:center;line-height:44px}
</style>
</head>
<body>

<section class="flyer flyer--front">
  <header class="masthead"><div class="brand">Pine Hill Drafting</div></header>
  <div class="masthead__rule"></div>
  <div class="plan-art" role="img" aria-label="Architectural floor plan with a rolled first floor plan sheet"></div>

  <div class="questions">
    <p>Are you planning to <span class="hl">RENOVATE,<br>EXTEND</span> the house, build new <span class="hl">GRANNY<br>FLAT?</span></p>
    <p>Do you need assistance with <span class="hl">DA,<br>COMPLYING DEVELOPMENT?</span></p>
    <p>Is your building budget tight and you<br><span class="hl">DON’T WANT</span> to spend it on the<br><span class="hl">ARCHITECTURAL FEES?</span></p>
  </div>

  <svg class="badge" viewBox="0 0 204 204" aria-hidden="true">
    <defs>
      <linearGradient id="badgeFill" x1="0" y1="0" x2="0" y2="1">
        <stop offset="0" stop-color="#3aa0d8"/>
        <stop offset="1" stop-color="#136fb0"/>
      </linearGradient>
    </defs>
    <g transform="translate(102 102)" fill="#fff" filter="drop-shadow(0 2px 2px rgba(0,0,0,.3))">
      <rect x="-70" y="-70" width="140" height="140"/>
      <rect x="-70" y="-70" width="140" height="140" transform="rotate(15)"/>
      <rect x="-70" y="-70" width="140" height="140" transform="rotate(30)"/>
      <rect x="-70" y="-70" width="140" height="140" transform="rotate(45)"/>
      <rect x="-70" y="-70" width="140" height="140" transform="rotate(60)"/>
      <rect x="-70" y="-70" width="140" height="140" transform="rotate(75)"/>
    </g>
    <g transform="translate(102 102)" fill="url(#badgeFill)">
      <rect x="-65" y="-65" width="130" height="130"/>
      <rect x="-65" y="-65" width="130" height="130" transform="rotate(15)"/>
      <rect x="-65" y="-65" width="130" height="130" transform="rotate(30)"/>
      <rect x="-65" y="-65" width="130" height="130" transform="rotate(45)"/>
      <rect x="-65" y="-65" width="130" height="130" transform="rotate(60)"/>
      <rect x="-65" y="-65" width="130" height="130" transform="rotate(75)"/>
    </g>
  </svg>
  <div class="badge__text">For free<br>obligation<br>quote<br>contact us!</div>

  <div class="contact">
    <div class="contact__name">PINE HILL DRAFTING</div>
    <div>pinehilldrafting@mailnest.net.au</div>
    <div>Dorte - 0482 657 930</div>
  </div>

  <footer class="footer-front">
    For more details check: www.pinehilldrafting.net.au<br>
    Follow us on chatterly: www.chatterly.net/pinehilldrafting
  </footer>
</section>

<section class="flyer flyer--back">
  <header class="masthead"><div class="brand">Pine Hill Drafting</div></header>
  <div class="masthead__rule"></div>
  <div class="house-art" role="img" aria-label="Line sketch of a small skillion-roof granny flat with deck and steps"></div>

  <ul class="services">
    <li class="services__title">Services</li>
    <li>- Building Design</li>
    <li>- Architectural Drafting</li>
    <li>- 3D Modelling</li>
    <li>- Norvo Assessment</li>
    <li>- Building Specifications</li>
    <li>- Council Submission Services</li>
    <li>- Coordination with Building Professionals</li>
  </ul>

  <div class="cta">Contact Dorte at 0482 657 930 or pinehilldrafting@mailnest.net.au<br>for obligation free quote!</div>

  <footer class="footer-back">For more details check: www.pinehilldrafting.net.au • Follow us on chatterly: www.chatterly.net/pinehilldrafting</footer>
</section>

</body>
</html>
```